Mobile phone signal boosting solutions needs a website

We need a website design for the reselling of a mobile signal boosting product set. These solutions are Vexlor exempt and will provide an indoor signal for mobile phones. We would like to see designs that incorporate the colours and feel of our logo. The domain will be
openmeadow.com / co.uk
Overview of the company and how it is to be used: Open meadow (domain name) will work with business and end user to provide mobile signal boosting – where people struggle indoors with a mobile signal our solutions will help by finding the smallest signal and boosting it, allowing users to use voice and data over their mobile network (please note this is not wireless signal boosting)
Number of Pages:
-Home
-Solutions / How it works
-Case Studies
-Contact
Text content: Currently just use placeholders
Technical specs : Wordpress and ability to use CMS if that’s relevant
Target Market(s)
Business professional all markets /high end residential
Coded - Design and coding required
4 page

```html
<!DOCTYPE html>
<html lang="en">
<head>
<meta charset="utf-8">
<title>Open Meadow – Mobile Signal Booster Solutions</title>
<link href="https://fonts.googleapis.com/css2?family=Roboto:ital,wght@0,400;0,500;0,700;1,500;1,700&display=swap" rel="stylesheet">
<style>
:root{
  --yellow:#fcc500;
  --yellow-deep:#f5b800;
  --ink:#111111;
  --text:#444444;
  --muted:#666666;
  --light:#f4f4f4;
  --line:#d6d6d6;
  --black:#0c0c0c;
  --white:#ffffff;
}
*{box-sizing:border-box;margin:0;padding:0}
html,body{width:1200px;height:4918px;overflow:hidden}
body{position:relative;font-family:'Roboto',sans-serif;color:var(--ink);background:var(--white)}
.abs{position:absolute}
.btn{position:absolute;background:var(--yellow);color:var(--ink);font-weight:700;font-size:15px;text-transform:uppercase;display:flex;align-items:center;justify-content:center;letter-spacing:.2px}
.section-title{position:absolute;left:0;width:1200px;text-align:center;font-weight:500;font-size:32px;text-transform:uppercase;line-height:1.25}

/* header */
.topline{left:0;top:0;width:1200px;height:6px;background:var(--yellow)}
.header{left:0;top:6px;width:1200px;height:104px;background:var(--white)}
.brand{position:absolute;display:flex;align-items:center;gap:10px;font-weight:500;color:var(--ink);white-space:nowrap}
.brand-mark{width:22px;height:22px;background:var(--yellow)}
.header .brand{left:149px;top:30px;font-size:30px}
.question{left:757px;top:0;width:293px;height:46px;background:var(--yellow);font-size:15px;font-weight:500;display:flex;align-items:center;justify-content:center;gap:8px}
.nav{left:535px;top:72px;display:flex;gap:63px;font-size:15px;font-weight:500;text-transform:uppercase}
.nav .active{color:var(--yellow)}

/* hero */
.hero{left:0;top:110px;width:1200px;height:672px;background:linear-gradient(90deg,#eeeeee 0%,#f3f3f3 40%,#e9e4de 100%)}
.hero-photo{left:430px;top:110px;width:770px;height:640px;background:linear-gradient(120deg,#f1f1f1 0%,#d8d3cc 45%,#c9b8a6 70%,#e8e6e4 100%)}
.hero-sub{left:151px;top:240px;font-size:30px;font-weight:500}
.hero-title{left:147px;top:288px;font-size:46px;font-weight:500;line-height:54px;text-transform:uppercase}

/* intro */
.intro{left:0;top:782px;width:1200px;height:530px;background:var(--light)}
.ring{border:5px solid var(--yellow);border-radius:50%;background:var(--white);padding:12px}
.ring .pic{width:100%;height:100%;border-radius:50%}
.intro-text{left:542px;top:874px;width:510px;font-size:18px;line-height:28px;color:var(--text)}
.intro-quote{left:540px;top:1062px;width:500px;font-size:21px;line-height:29px;font-style:italic;font-weight:700;color:var(--ink)}
.intro-cite{left:538px;top:1166px;font-size:23px;font-style:italic;font-weight:500;color:var(--yellow)}

/* where */
.where-grid{left:134px;top:1469px;display:flex;gap:10px}
.where-card{width:180px;height:194px;border:1.5px solid var(--line);display:flex;flex-direction:column;align-items:center;padding-top:24px}
.where-card svg{width:62px;height:60px}
.where-card p{margin-top:22px;width:145px;text-align:center;font-size:13px;line-height:16px;color:var(--muted)}

/* about */
.about{left:0;top:1726px;width:1200px;height:602px;background:var(--light)}
.about-title{left:149px;top:1844px;font-size:32px;font-weight:500}
.about-text{left:149px;top:1904px;width:430px;font-size:14px;line-height:22px;color:var(--text)}
.about-text p+p{margin-top:22px}

/* clients */
.clients-grid{left:153px;top:2520px;display:grid;grid-template-columns:repeat(3,277px);column-gap:33px;row-gap:29px}
.client{position:relative;height:252px;overflow:hidden}
.client .pic{position:absolute;inset:0}
.client .shade{position:absolute;inset:0;background:linear-gradient(180deg,rgba(0,0,0,0) 40%,rgba(0,0,0,.55) 100%)}
.client h3{position:absolute;left:0;right:0;bottom:52px;text-align:center;color:var(--white);font-size:19px;font-weight:700}
.client svg{position:absolute;left:126px;bottom:24px}

/* services */
.services{left:0;top:3148px;width:1200px;height:512px;background:var(--yellow)}
.services-title{left:0;top:3228px;width:1200px;text-align:center;font-size:42px;font-weight:700;text-transform:uppercase}
.services-rule{left:550px;top:3290px;width:100px;height:4px;background:var(--ink)}
.step{position:absolute;top:3340px;width:170px;text-align:center}
.step svg.icon{width:80px;height:80px;display:block;margin:0 auto}
.step .num{width:32px;height:32px;border-radius:50%;background:var(--ink);color:var(--white);font-weight:700;font-size:17px;display:flex;align-items:center;justify-content:center;margin:22px auto 0}
.step p{margin-top:14px;font-size:16px;line-height:19px;color:var(--ink)}

/* networks */
.networks-title{left:0;top:3756px;width:1200px;text-align:center;font-size:15px;font-weight:500;text-transform:uppercase}
.networks{left:382px;top:3805px;display:flex}
.net{width:146px;height:78px;border:1.5px solid var(--line);display:flex;align-items:center;justify-content:center;font-size:22px;font-weight:700;color:var(--ink)}
.net+.net{margin-left:-1.5px}

/* contact */
.contact-title{left:0;top:3964px;width:1200px;text-align:center;font-size:32px;font-weight:500;text-transform:uppercase}
.contact-lead{left:290px;top:4026px;width:620px;text-align:center;font-size:14px;line-height:22px;color:var(--muted)}
.field{position:absolute;border:1.5px solid #bfbfbf;background:var(--white);font-size:12px;color:var(--muted);padding:10px 10px}

/* footer */
.footer-brand{left:150px;top:4630px;width:190px;flex-direction:column;gap:14px;font-size:30px;color:var(--white);font-weight:500}
.footer-brand .brand-mark{width:40px;height:40px}
.fcol{position:absolute;top:4608px}
.fcol h4{font-size:15px;font-weight:700;color:var(--white);text-transform:uppercase}
.fcol .rule{position:relative;width:140px;height:1px;background:#666;margin-top:18px}
.fcol .rule::before{content:"";position:absolute;left:0;top:-3px;width:10px;height:7px;background:var(--yellow)}
.fcol ul{list-style:none;margin-top:26px;color:var(--white);font-size:14px}
.fcol li{height:24px;display:flex;align-items:center;gap:12px}
.fcol.contacts li{height:48px}
.fcol.social li{height:48px}
.dot{width:26px;height:26px;border-radius:50%;background:var(--yellow);display:flex;align-items:center;justify-content:center}
.sq{width:16px;height:16px;background:var(--yellow)}
.copyright{left:0;top:4870px;width:1200px;text-align:center;font-size:11px;color:var(--white)}
</style>
</head>
<body>

<!-- header -->
<div class="abs topline"></div>
<header class="abs header">
  <div class="brand"><span class="brand-mark"></span>Open Meadow</div>
</header>
<div class="abs question">
  <svg width="14" height="14" viewBox="0 0 24 24"><path d="M6.6 10.8a15 15 0 0 0 6.6 6.6l2.2-2.2c.3-.3.7-.4 1-.2 1.1.4 2.3.6 3.6.6.6 0 1 .4 1 1V20c0 .6-.4 1-1 1A17 17 0 0 1 3 4c0-.6.4-1 1-1h3.5c.6 0 1 .4 1 1 0 1.3.2 2.5.6 3.6.1.3 0 .7-.2 1z" fill="#111"/></svg>
  Have a question?: 01632 960418
</div>
<nav class="abs nav">
  <span class="active">Home</span><span>The Process</span><span>Solutions</span><span>Contact</span>
</nav>

<!-- hero -->
<section class="abs hero"></section>
<div class="abs hero-photo" role="img" aria-label="Doctor showing an older woman something on a mobile phone beside a potted plant"></div>
<svg class="abs" style="left:0;top:690px" width="1200" height="92" viewBox="0 0 1200 92">
  <polygon points="0,92 0,70 560,70 1200,0 1200,92" fill="#f4f4f4"/>
  <polygon points="560,55 1200,0 1200,92 860,70 " fill="#fcc500"/>
  <polygon points="0,60 560,55 860,70 0,70" fill="#f4f4f4"/>
</svg>
<div class="abs hero-sub">Open Meadow</div>
<h1 class="abs hero-title">Mobile Signal<br>Booster Solutions</h1>
<div class="btn" style="left:149px;top:410px;width:166px;height:44px">Find Out More</div>

<!-- intro -->
<section class="abs intro"></section>
<div class="abs ring" style="left:158px;top:864px;width:336px;height:336px">
  <div class="pic" role="img" aria-label="Scientist in a lab coat working at a laboratory bench" style="background:linear-gradient(135deg,#e9eef1,#c4ccd2 55%,#8b98a2)"></div>
</div>
<p class="abs intro-text">As the world constantly evolves and expand we are experiencing an ever-increasing reliance on Communication and Data for both social and commercial interaction. The reliance on an always available and strong cellular network is critical today and will continue to grow with technological developments in the future.</p>
<p class="abs intro-quote">“What's the biggest function of a cell phone? What does a cell phone do for humanity? It makes people more productive.”</p>
<p class="abs intro-cite">Arlen Pryce - Scientist</p>

<!-- where -->
<h2 class="section-title" style="top:1388px">Where do you need to boost signal?</h2>
<div class="abs where-grid">
  <div class="where-card">
    <svg viewBox="0 0 62 60" fill="none" stroke="#222" stroke-width="2"><rect x="8" y="14" width="22" height="42" fill="#fcc500"/><rect x="30" y="26" width="24" height="30"/><path d="M4 56h54M14 22h4M22 22h4M14 32h4M22 32h4M14 42h4M22 42h4M36 34h4M44 34h4M36 44h4M44 44h4"/></svg>
    <p>Lorem ipsum dolor amet, consectetur adip iscing elit, sedeiu.</p>
  </div>
  <div class="where-card">
    <svg viewBox="0 0 62 60" fill="none" stroke="#222" stroke-width="2"><rect x="10" y="16" width="42" height="40"/><rect x="24" y="4" width="14" height="12" fill="#fcc500"/><path d="M31 7v6M28 10h6M4 56h54M16 24h6M40 24h6M16 34h6M40 34h6M26 44h10v12H26z"/></svg>
    <p>Lorem ipsum dolor amet, consectetur adip iscing elit, sedeiu.</p>
  </div>
  <div class="where-card">
    <svg viewBox="0 0 62 60" fill="none" stroke="#222" stroke-width="2"><path d="M6 24 31 6l25 18v32H6z" fill="#fcc500"/><rect x="16" y="30" width="30" height="26" fill="#fff"/><path d="M16 38h30M16 46h30M4 56h54"/></svg>
    <p>Lorem ipsum dolor amet, consectetur adip iscing elit, sedeiu.</p>
  </div>
  <div class="where-card">
    <svg viewBox="0 0 62 60" fill="none" stroke="#222" stroke-width="2"><rect x="6" y="20" width="50" height="10" fill="#fcc500"/><rect x="10" y="30" width="42" height="26"/><rect x="22" y="4" width="18" height="16"/><path d="M4 56h54M16 38h10v10H16zM36 38h10v18H36z"/></svg>
    <p>Lorem ipsum dolor amet, consectetur adip iscing elit, sedeiu.</p>
  </div>
  <div class="where-card">
    <svg viewBox="0 0 62 60" fill="none" stroke="#222" stroke-width="2"><path d="M6 32 26 16l20 16" /><rect x="10" y="32" width="32" height="24" fill="#fcc500"/><circle cx="48" cy="18" r="9"/><path d="M48 27v29M4 56h54M22 42h8v14h-8z"/></svg>
    <p>Lorem ipsum dolor amet, consectetur adip iscing elit, sedeiu.</p>
  </div>
</div>

<!-- about -->
<section class="abs about"></section>
<h2 class="abs about-title">ABOUT US</h2>
<div class="abs about-text">
  <p>The team at openmeadow.com listen to you to understand the limitations and problems you are facing as a result of poor indoor mobile coverage.  We assess your individual issues and design signal boosting solutions to match and exceed your requirements and expectations.</p>
  <p>We provide market leading Vexlor licence exempt mobile signal booster solutions, to ensure the complete availability of 3g,4g and 5g connectivity technology across the major cellular carriers including Voltan, Orbis, Eastel and Trio.</p>
</div>
<div class="btn" style="left:149px;top:2148px;width:146px;height:44px">Read More</div>
<div class="abs ring" style="left:628px;top:1816px;width:420px;height:420px">
  <div class="pic" role="img" aria-label="Two colleagues looking at a tablet and a phone together" style="background:linear-gradient(135deg,#d9d6d2,#b7aca0 50%,#8c7c6c)"></div>
</div>

<!-- clients -->
<h2 class="section-title" style="top:2398px">Typical Clients<br>Explore by client type</h2>
<div class="abs clients-grid">
  <div class="client"><div class="pic" role="img" aria-label="Woman using a phone in an office" style="background:linear-gradient(135deg,#3a4148,#8a8580 60%,#cfc7bd)"></div><div class="shade"></div><h3>Offices</h3><svg width="24" height="12" viewBox="0 0 24 12"><path d="M0 6h22M17 1l5 5-5 5" stroke="#fcc500" stroke-width="2" fill="none"/></svg></div>
  <div class="client"><div class="pic" role="img" aria-label="Older woman smiling at a phone in a bright room" style="background:linear-gradient(135deg,#e6e8ea,#b6c3cc 55%,#7f909c)"></div><div class="shade"></div><h3>Health</h3><svg width="24" height="12" viewBox="0 0 24 12"><path d="M0 6h22M17 1l5 5-5 5" stroke="#fcc500" stroke-width="2" fill="none"/></svg></div>
  <div class="client"><div class="pic" role="img" aria-label="Man holding a phone in a warehouse aisle" style="background:linear-gradient(135deg,#6a4e35,#9b7a58 50%,#3b3f47)"></div><div class="shade"></div><h3>Factories &amp; Warehouses</h3><svg width="24" height="12" viewBox="0 0 24 12"><path d="M0 6h22M17 1l5 5-5 5" stroke="#fcc500" stroke-width="2" fill="none"/></svg></div>
  <div class="client"><div class="pic" role="img" aria-label="Woman on a phone in a hotel room" style="background:linear-gradient(135deg,#5a4232,#a07f62 55%,#d6c2a8)"></div><div class="shade"></div><h3>Hospitality/Recreation</h3><svg width="24" height="12" viewBox="0 0 24 12"><path d="M0 6h22M17 1l5 5-5 5" stroke="#fcc500" stroke-width="2" fill="none"/></svg></div>
  <div class="client"><div class="pic" role="img" aria-label="Shopper with bags on a phone in a mall" style="background:linear-gradient(135deg,#c9c7c1,#a6a39c 50%,#6e6a64)"></div><div class="shade"></div><h3>Retail</h3><svg width="24" height="12" viewBox="0 0 24 12"><path d="M0 6h22M17 1l5 5-5 5" stroke="#fcc500" stroke-width="2" fill="none"/></svg></div>
  <div class="client"><div class="pic" role="img" aria-label="Couple relaxing at home with a phone" style="background:linear-gradient(135deg,#3d2a4a,#7c6a80 50%,#d9d3cc)"></div><div class="shade"></div><h3>Residential</h3><svg width="24" height="12" viewBox="0 0 24 12"><path d="M0 6h22M17 1l5 5-5 5" stroke="#fcc500" stroke-width="2" fill="none"/></svg></div>
</div>

<!-- services -->
<section class="abs services"></section>
<h2 class="abs services-title">Our Services</h2>
<div class="abs services-rule"></div>
<svg class="abs" style="left:0;top:3420px" width="1200" height="60" viewBox="0 0 1200 60"><path d="M0 18 C80 10 150 60 221 37 S330 8 410 37 S520 10 599 37 S700 8 788 37 S900 10 977 37 S1100 20 1200 6" stroke="#111" stroke-width="2" stroke-dasharray="3 4" fill="none"/></svg>
<div class="step" style="left:136px">
  <svg class="icon" viewBox="0 0 80 80" fill="none" stroke="#111" stroke-width="2.5"><rect x="36" y="4" width="30" height="18" rx="4"/><circle cx="22" cy="44" r="8"/><circle cx="54" cy="44" r="8"/><path d="M8 74c0-10 6-16 14-16s14 6 14 16M40 74c0-10 6-16 14-16s14 6 14 16M18 10h12v10l-4-3h-8z"/></svg>
  <div class="num">1</div><p>Initial conversation, identifying problem areas and impact</p>
</div>
<div class="step" style="left:325px">
  <svg class="icon" viewBox="0 0 80 80" fill="none" stroke="#111" stroke-width="2.5"><path d="M16 30a16 16 0 0 1 32 0z"/><path d="M12 30h40"/><circle cx="32" cy="40" r="8"/><path d="M12 76V62c0-8 8-12 20-12s20 4 20 12v14"/><rect x="58" y="6" width="14" height="34"/><path d="M65 40v36"/></svg>
  <div class="num">2</div><p>Survey onsite, this will help us put together the best solution</p>
</div>
<div class="step" style="left:514px">
  <svg class="icon" viewBox="0 0 80 80" fill="none" stroke="#111" stroke-width="2.5"><circle cx="50" cy="24" r="16"/><path d="M50 14v20M55 18h-7a3 3 0 0 0 0 6h4a3 3 0 0 1 0 6h-7"/><path d="M8 46h12v28H8zM20 50h20l8 4-8 16H20"/></svg>
  <div class="num">3</div><p>Review of solution and pricing</p>
</div>
<div class="step" style="left:703px">
  <svg class="icon" viewBox="0 0 80 80" fill="none" stroke="#111" stroke-width="2.5"><path d="M14 8a12 12 0 0 0 14 16l38 38-6 6-38-38A12 12 0 0 1 6 16l8 6 6-6z"/><path d="M50 14l16 16M60 8l12 12-6 6-12-12zM12 68l20-20"/></svg>
  <div class="num">4</div><p>Installation</p>
</div>
<div class="step" style="left:892px">
  <svg class="icon" viewBox="0 0 80 80" fill="none" stroke="#111" stroke-width="2.5"><path d="M18 36a20 20 0 0 1 40 0"/><rect x="12" y="34" width="10" height="14" rx="3"/><rect x="54" y="34" width="10" height="14" rx="3"/><circle cx="38" cy="42" r="10"/><path d="M16 76c0-12 10-18 22-18s22 6 22 18M52 6h20v12H60l-4 4v-4h-4z"/></svg>
  <div class="num">5</div><p>Review and support</p>
</div>

<!-- networks -->
<p class="abs networks-title">Works for 2G, 3G, and 4G LTE networks on all carriers</p>
<div class="abs networks">
  <div class="net">Voltan</div><div class="net">Orbis</div><div class="net">Trio</div>
</div>

<!-- contact -->
<h2 class="abs contact-title">Contact Us</h2>
<p class="abs contact-lead">Lorem ipsum dolor sit amet, consectetur adipiscing elit, sed do eiusmod tempor incididunt ut labore et dolore magna aliquais ipsum suspendisse ultrices gravidaus commod</p>
<div class="field" style="left:279px;top:4102px;width:210px;height:38px">Name</div>
<div class="field" style="left:496px;top:4102px;width:210px;height:38px">Email</div>
<div class="field" style="left:713px;top:4102px;width:210px;height:38px">Phone</div>
<div class="field" style="left:279px;top:4150px;width:644px;height:144px">Message</div>
<div class="btn" style="left:532px;top:4270px;width:136px;height:46px;font-size:14px">Submit Now</div>

<!-- footer -->
<svg class="abs" style="left:0;top:4390px" width="1200" height="528" viewBox="0 0 1200 528">
  <defs><linearGradient id="band" x1="0" x2="1" y1="0" y2="0"><stop offset="0" stop-color="#fcc500"/><stop offset=".6" stop-color="#fcc500"/><stop offset="1" stop-color="#6d5600"/></linearGradient></defs>
  <polygon points="0,10 1200,150 1200,528 0,528" fill="#0c0c0c"/>
  <polygon points="0,8 1200,120 1200,180 0,55" fill="url(#band)"/>
  <polygon points="0,55 1200,180 1200,528 0,528" fill="#0c0c0c"/>
</svg>
<div class="brand footer-brand"><span class="brand-mark"></span>Open Meadow</div>
<div class="fcol" style="left:391px">
  <h4>Quick Links</h4><div class="rule"></div>
  <ul><li>Home</li><li>The process</li><li>Solutions</li><li>Contact</li></ul>
</div>
<div class="fcol contacts" style="left:603px">
  <h4>Contact</h4><div class="rule"></div>
  <ul>
    <li><span class="dot"><svg width="14" height="10" viewBox="0 0 14 10"><rect x=".5" y=".5" width="13" height="9" fill="none" stroke="#111"/><path d="M.5 .5 7 5.5 13.5 .5" fill="none" stroke="#111"/></svg></span>info@openmeadow.com</li>
    <li><span class="dot"><svg width="13" height="13" viewBox="0 0 24 24"><path d="M6.6 10.8a15 15 0 0 0 6.6 6.6l2.2-2.2c.3-.3.7-.4 1-.2 1.1.4 2.3.6 3.6.6.6 0 1 .4 1 1V20c0 .6-.4 1-1 1A17 17 0 0 1 3 4c0-.6.4-1 1-1h3.5c.6 0 1 .4 1 1 0 1.3.2 2.5.6 3.6.1.3 0 .7-.2 1z" fill="#111"/></svg></span>Call: 01632 960418</li>
  </ul>
</div>
<div class="fcol social" style="left:881px">
  <h4>Follow Me</h4><div class="rule"></div>
  <ul><li><span class="sq"></span>Newsfeed</li><li><span class="sq"></span>Chirper</li><li><span class="sq"></span>Workline</li></ul>
</div>
<p class="abs copyright">Copyright © 2023 | Open Meadow. All rights Reserved</p>

</body>
</html>
```